Picket Sign Advertising For Alaska Tour Company

I would like a relator style picket sign made that I can place by the water near hotels to generate phone calls and website visits. I want to Advertise Our Daily Jet Boat Tours & Jet Ski Tours. This will be a one sided sign. You may be able to see our past brochure and flyer designs and logo. Our FB page is Harlow Summit Excursions and our website is harlowsummitexcursions.com or contact number is 907-518-4463

```html
<!DOCTYPE html>
<html lang="en">
<head>
<meta charset="utf-8">
<title>Harlow Summit Excursions – Picket Sign</title>
<link href="https://fonts.googleapis.com/css2?family=Cinzel:wght@600;700&family=Montserrat:wght@500;700&display=swap" rel="stylesheet">
<style>
  :root {
    --navy: #0f2a5e;
    --gold: #dcb865;
    --gold-light: #f1d98f;
    --cream: #f3ead2;
    --white: #ffffff;
    --sky-top: #6b6fb5;
    --sky-glow: #f2c6b8;
    --hill: #233259;
    --water: #b88ad0;
  }
  * { box-sizing: border-box; margin: 0; padding: 0; }
  html, body { width: 1200px; height: 800px; overflow: hidden; background: #fff; }
  .sign {
    position: relative;
    width: 1200px;
    height: 800px;
    overflow: hidden;
    font-family: "Montserrat", sans-serif;
  }
  .scenery {
    position: absolute;
    inset: 0;
    background:
      linear-gradient(180deg,
        var(--sky-top) 0%,
        #b59ac6 12%,
        var(--sky-glow) 22%,
        #d8a7c4 28%,
        var(--hill) 33%,
        #2b3553 46%,
        #6c5a8a 52%,
        var(--water) 62%,
        #9c78c6 80%,
        #8a6abb 100%);
  }
  .headline {
    position: absolute;
    left: 0;
    top: 70px;
    width: 1200px;
    text-align: center;
    font-family: "Cinzel", serif;
    font-weight: 700;
    font-size: 46px;
    letter-spacing: 3px;
    line-height: 1.15;
    color: var(--white);
  }
  .headline-sub {
    display: block;
    margin-top: 10px;
    font-family: "Montserrat", sans-serif;
    font-weight: 700;
    font-size: 20px;
    letter-spacing: 8px;
    color: var(--navy);
  }
  .band {
    position: absolute;
    inset: 0;
    width: 1200px;
    height: 800px;
  }
  .brand {
    position: absolute;
    left: 40px;
    top: 622px;
    width: 560px;
  }
  .brand-name {
    font-family: "Cinzel", serif;
    font-weight: 600;
    font-size: 44px;
    letter-spacing: 1px;
    color: var(--gold);
    line-height: 1;
    white-space: nowrap;
  }
  .brand-sub {
    margin-top: 12px;
    font-family: "Montserrat", sans-serif;
    font-weight: 500;
    font-size: 20px;
    letter-spacing: 9px;
    color: var(--cream);
    line-height: 1;
  }
  .brand-rule {
    margin-top: 10px;
    width: 360px;
    height: 2px;
    background: var(--gold);
  }
  .tagline {
    margin-top: 24px;
    font-weight: 500;
    font-size: 14px;
    letter-spacing: 6.2px;
    color: var(--cream);
    white-space: nowrap;
  }
  .contact {
    position: absolute;
    right: 42px;
    top: 704px;
  }
  .contact-line {
    display: flex;
    align-items: center;
    gap: 8px;
  }
  .contact-web {
    font-weight: 700;
    font-size: 22px;
    color: var(--gold-light);
  }
  .contact-phone {
    margin-top: 2px;
    font-weight: 700;
    font-size: 48px;
    letter-spacing: 0.5px;
    line-height: 1.1;
    color: var(--gold);
  }
  .icon { flex: none; }
</style>
</head>
<body>
<main class="sign">
  <div class="scenery" role="img" aria-label="Photo of a calm river at sunset with purple and pink sky, dark hills, bare trees and a house reflected in the water"></div>

  <h2 class="headline">Daily Jet Boat &amp; Jet Ski Tours
    <span class="headline-sub">BOOK YOUR RIDE TODAY</span>
  </h2>

  <svg class="band" viewBox="0 0 1200 800" aria-hidden="true">
    <path d="M0 500 C 260 470, 520 560, 760 650 C 930 712, 1080 680, 1200 612 L1200 800 L0 800 Z" fill="var(--navy)"/>
    <path d="M0 500 C 260 470, 520 560, 760 650 C 930 712, 1080 680, 1200 612" fill="none" stroke="var(--gold)" stroke-width="5"/>
  </svg>

  <section class="brand">
    <h1 class="brand-name">HARLOW SUMMIT</h1>
    <p class="brand-sub">EXCURSIONS</p>
    <div class="brand-rule"></div>
    <p class="tagline">TAKING YOU WHERE YOU WANT TO GO</p>
  </section>

  <section class="contact">
    <div class="contact-line contact-web">
      <svg class="icon" width="20" height="20" viewBox="0 0 22 22" aria-hidden="true">
        <g fill="none" stroke="var(--gold-light)" stroke-width="1.8">
          <circle cx="11" cy="11" r="9"/>
          <ellipse cx="11" cy="11" rx="4" ry="9"/>
          <line x1="2" y1="11" x2="20" y2="11"/>
        </g>
      </svg>
      <span>www.harlowsummitexcursions.com</span>
    </div>
    <div class="contact-line contact-phone">
      <svg class="icon" width="40" height="40" viewBox="0 0 38 38" aria-hidden="true">
        <circle cx="19" cy="19" r="18" fill="var(--gold)"/>
        <path d="M13 10 l4 0 l2 6 l-3 2 c1.5 3 3 4.5 6 6 l2 -3 l6 2 l0 4 c0 1 -1 2 -2 2 c-9 0 -17 -8 -17 -17 c0 -1 1 -2 2 -2 z" fill="var(--navy)"/>
      </svg>
      <span>907-518-4463</span>
    </div>
  </section>
</main>
</body>
</html>
```